Bref créative
Grace & Vow
Building Bridges For Marriage
Professional
Darnel & Lucinda Hayward
Pastor and First Lady
PO Box 7816
Hollowell WV.25719
rut417@bk-fell.org
www.bk-fell.org

```html
<!DOCTYPE html>
<html lang="en">
<head>
<meta charset="utf-8">
<title>Grace &amp; Vow — Business Cards</title>
<link rel="stylesheet" href="https://fonts.googleapis.com/css2?family=Open+Sans:wght@400;600;700&family=Cinzel:wght@600&display=swap">
<style>
  :root {
    --page-bg: #e9e6e1;
    --card-black: #0b0b0b;
    --card-black-edge: #1c1c1c;
    --red-deep: #3a0407;
    --red-mid: #8e0f18;
    --red-glow: #c4202b;
    --gold: #d9b25a;
    --gold-light: #f0d48a;
    --tagline-red: #c8232e;
    --tagline-pink: #f08a8f;
    --text-white: #f4f1ec;
    --text-soft: #cfcac2;
  }
  * { box-sizing: border-box; margin: 0; padding: 0; }
  html, body {
    width: 1200px; height: 804px; overflow: hidden;
    background: var(--page-bg);
    font-family: "Open Sans", Arial, sans-serif;
  }
  .sheet {
    width: 1200px; height: 804px;
    display: flex; align-items: center; justify-content: center; gap: 40px;
  }
  .card {
    position: relative;
    width: 560px; height: 320px;
    border-radius: 4px;
    overflow: hidden;
    box-shadow: 0 6px 18px rgba(0,0,0,0.22);
  }

  /* Contact side */
  .card--contact {
    background: linear-gradient(135deg, var(--card-black-edge) 0%, var(--card-black) 55%, #000 100%);
    color: var(--text-white);
    padding: 34px 36px;
  }
  .brand { display: inline-flex; flex-direction: column; }
  .brand-name {
    font-weight: 700;
    color: var(--gold);
    line-height: 1;
    letter-spacing: 0.5px;
  }
  .card--contact .brand-name { font-size: 40px; }
  .tagline {
    font-family: "Cinzel", Georgia, serif;
    font-weight: 600;
    color: var(--tagline-red);
    text-transform: uppercase;
    letter-spacing: 0.6px;
  }
  .card--contact .tagline { font-size: 11.5px; margin-top: 8px; }
  .scripture {
    font-family: "Cinzel", Georgia, serif;
    font-weight: 600;
    color: var(--gold);
    text-transform: uppercase;
    letter-spacing: 1px;
    align-self: flex-end;
  }
  .card--contact .scripture { font-size: 7.5px; margin-top: 3px; }
  .holder { margin-top: 26px; }
  .holder-names { font-size: 15px; font-weight: 700; color: var(--gold); }
  .holder-title { font-size: 12px; color: var(--text-white); margin-top: 2px; }
  .contact-list { list-style: none; margin-top: 14px; font-size: 11.5px; color: var(--text-soft); }
  .contact-list li { display: flex; align-items: center; gap: 8px; margin-bottom: 5px; }
  .contact-icon {
    width: 15px; height: 15px; border-radius: 50%;
    background: var(--gold);
    display: flex; align-items: center; justify-content: center;
    flex: none;
  }
  .postal { font-size: 11.5px; color: var(--text-soft); margin-top: 8px; }

  /* Front side */
  .card--front {
    background: radial-gradient(ellipse 70% 75% at 50% 42%, var(--red-glow) 0%, var(--red-mid) 45%, var(--red-deep) 100%);
    display: flex; flex-direction: column; align-items: center; justify-content: center;
    text-align: center;
    padding-bottom: 40px;
  }
  .card--front .brand-name { font-size: 58px; color: var(--gold-light); }
  .card--front .tagline { font-size: 16px; margin-top: 10px; color: var(--tagline-pink); }
  .card--front .scripture { font-size: 9px; margin-top: 4px; }
  .web-address {
    position: absolute; bottom: 48px; left: 0; right: 0;
    font-size: 19px; font-weight: 600; color: var(--text-white);
    letter-spacing: 2.5px;
  }
</style>
</head>
<body>
<main class="sheet">
  <section class="card card--contact" aria-label="Business card, contact side">
    <div class="brand">
      <div class="brand-name">Grace &amp; Vow</div>
      <div class="tagline">Building Bridges For Marriage</div>
      <div class="scripture">Ephesians 5:33</div>
    </div>
    <div class="holder">
      <div class="holder-names">Darnel &amp; Lucinda Hayward</div>
      <div class="holder-title">Pastor and First Lady</div>
    </div>
    <ul class="contact-list">
      <li>
        <span class="contact-icon">
          <svg width="9" height="9" viewBox="0 0 24 24" aria-hidden="true"><path fill="#0b0b0b" d="M6.6 10.8a15.1 15.1 0 0 0 6.6 6.6l2.2-2.2c.3-.3.7-.4 1-.2 1.1.4 2.3.6 3.6.6.6 0 1 .4 1 1V20c0 .6-.4 1-1 1A17 17 0 0 1 3 4c0-.6.4-1 1-1h3.5c.6 0 1 .4 1 1 0 1.3.2 2.5.6 3.6.1.3 0 .7-.2 1z"/></svg>
        </span>
        240-555-0142
      </li>
      <li>
        <span class="contact-icon">
          <svg width="9" height="9" viewBox="0 0 24 24" aria-hidden="true"><path fill="#0b0b0b" d="M2 5h20v14H2z"/><path d="M2 5l10 8 10-8" stroke="#d9b25a" stroke-width="2" fill="none"/></svg>
        </span>
        rut417@bk-fell.org
      </li>
      <li>
        <span class="contact-icon">
          <svg width="9" height="9" viewBox="0 0 24 24" aria-hidden="true"><circle cx="12" cy="12" r="9" fill="none" stroke="#0b0b0b" stroke-width="2.4"/><path d="M3 12h18M12 3c3 3 3 15 0 18M12 3c-3 3-3 15 0 18" fill="none" stroke="#0b0b0b" stroke-width="2"/></svg>
        </span>
        www.bk-fell.org
      </li>
    </ul>
    <div class="postal">PO Box 7816, Hollowell KY.25719</div>
  </section>

  <section class="card card--front" aria-label="Business card, front side">
    <div class="brand">
      <div class="brand-name">Grace &amp; Vow</div>
      <div class="tagline">Building Bridges For Marriage</div>
      <div class="scripture">Ephesians 5:33</div>
    </div>
    <div class="web-address">www.bk-fell.org</div>
  </section>
</main>
</body>
</html>
```